Course flyer - evolutive design

We want to have a nice design for our course programm.
In fact we are school language, and our course programm change approximatively each 2 weeks§.
For that we need a design that we can modify each 2 weeks (only dates change ) by ourselves.
We used to have a classical design but we want to upgrade it with a modern and attractive design.
We can have 3 versions one for each city.
We have 3 offices: Tunis, Sousse & Sfax
Attached you can find old designs

Target Market(s)

students from 16 years old till retired people 76 years old

Industry/Entity Type

Education

Font styles to use
Sans Serif

Requirements
Must have
• clear timing for courses (date, days, timing)
• prices
• Adresse (each flyer has its own adress)
• phone Number
• Cool image
Should not have
• Racism
• Violence
• Too much stuff

```html
<!DOCTYPE html>
<html lang="fr">
<head>
<meta charset="utf-8">
<title>Cours d'allemand – Linguora Centre</title>
<link href="https://fonts.googleapis.com/css2?family=Teko:wght@500;600&family=Lato:wght@400;700;900&display=swap" rel="stylesheet">
<style>
  :root{
    --lime:#cbd636;
    --lime-light:#e3ea7a;
    --lime-dark:#a9b21c;
    --ink:#111111;
    --paper:#ffffff;
    --grey:#333333;
  }
  *{box-sizing:border-box;margin:0;padding:0}
  html,body{width:907px;height:1200px;overflow:hidden;background:var(--paper)}
  body{font-family:"Lato",Arial,sans-serif;color:var(--ink)}
  .flyer{position:relative;width:907px;height:1200px;overflow:hidden;background:var(--paper)}

  /* Brand */
  .brand{position:absolute;left:40px;top:150px;display:flex;align-items:center;gap:12px;z-index:2}
  .brand-dot{width:26px;height:26px;border-radius:50%;background:var(--lime);flex:none}
  .brand-name{display:flex;flex-direction:column;align-items:flex-end;font-family:"Teko",sans-serif;font-weight:600;color:var(--ink);line-height:0.85}
  .brand-name .main{font-size:72px}
  .brand-name .sub{font-size:72px}

  /* Hero */
  .hero{position:absolute;left:0;top:0;width:907px;height:410px}

  /* Title band */
  .title-band{position:absolute;left:0;top:418px;width:565px;height:88px;background:var(--ink);
    display:flex;align-items:center;justify-content:center}
  .title-band h1{font-family:"Teko",sans-serif;font-weight:500;font-size:78px;letter-spacing:2px;color:var(--paper);line-height:1;padding-top:10px}
  .period-band{position:absolute;left:572px;top:418px;width:335px;height:88px;background:var(--lime);
    display:flex;align-items:center;justify-content:center}
  .period-band span{font-family:"Teko",sans-serif;font-weight:500;font-size:56px;letter-spacing:2px;color:var(--ink);line-height:1;padding-top:8px}

  /* Section labels */
  .label{position:absolute;display:flex;align-items:center;gap:6px;font-weight:700;font-size:17px}
  .label .tag{background:var(--lime);color:var(--paper);font-weight:900;font-size:22px;padding:0 4px;line-height:28px}
  .label.large{font-weight:400;font-size:22px}

  /* Schedule */
  .schedule{position:absolute}
  .schedule-date{background:var(--ink);color:var(--paper);font-weight:900;font-size:28px;text-align:center;
    border-radius:14px 14px 6px 6px;height:56px;line-height:56px;margin:0 -4px;position:relative;z-index:1}
  .schedule-times{display:flex;justify-content:space-around;font-size:17px;
    background:linear-gradient(90deg,var(--lime-dark),var(--lime) 40%,var(--lime-light));height:34px;line-height:34px;margin-top:-4px;padding-top:2px}
  .schedule-times.single{justify-content:center;height:42px;line-height:44px}
  .schedule-rows{display:grid;grid-template-columns:1fr 1fr;background:var(--paper)}
  .schedule-rows div{font-size:14px;height:28px;line-height:24px;padding-left:30px;
    border-bottom:5px solid transparent;border-image:linear-gradient(90deg,var(--lime-dark),var(--lime) 50%,var(--lime-light)) 1}
  .schedule-rows b{font-weight:900}
  .schedule-foot{height:34px;border-radius:0 0 14px 14px;
    background:linear-gradient(90deg,var(--lime-dark),var(--lime) 40%,var(--lime-light))}
  .schedule-foot.thin{height:12px}

  .notes{position:absolute;left:491px;top:830px;width:366px;font-size:13px;line-height:17px;color:var(--grey)}

  .students{position:absolute;left:473px;top:918px;width:380px;height:282px}

  /* Footer */
  .footer{position:absolute;left:0;top:1096px;width:907px;height:104px;background:var(--ink);color:var(--paper);font-size:14px;line-height:19px}
  .footer .address{position:absolute;left:22px;top:18px;width:330px;display:flex;gap:6px}
  .footer .contacts{position:absolute;left:360px;top:14px;list-style:none}
  .footer .contacts li{display:flex;align-items:center;gap:8px;height:24px}
  .icon{flex:none}
</style>
</head>
<body>
<main class="flyer">

  <svg class="hero" viewBox="0 0 907 410">
    <defs>
      <linearGradient id="photoTone" x1="0" y1="0" x2="1" y2="1">
        <stop offset="0" stop-color="#b79c7a"/>
        <stop offset="0.45" stop-color="#d9c6ae"/>
        <stop offset="1" stop-color="#6f8fb0"/>
      </linearGradient>
    </defs>
    <polygon points="420,0 907,0 907,350 360,350" fill="url(#photoTone)" role="img" aria-label="Photo: groupe d'étudiants travaillant ensemble dans une bibliothèque"/>
    <polygon points="400,0 420,0 360,350 340,350" fill="var(--lime)"/>
    <polygon points="368,0 392,0 334,350 310,350" fill="var(--ink)"/>
    <polygon points="560,360 907,360 907,380 552,380" fill="var(--ink)"/>
    <polygon points="685,385 907,385 907,402 680,402" fill="var(--lime)"/>
  </svg>

  <div class="brand">
    <span class="brand-dot"></span>
    <span class="brand-name"><span class="main">Linguora</span><span class="sub">Centre</span></span>
  </div>

  <div class="title-band"><h1>COURS D’ALLEMAND</h1></div>
  <div class="period-band"><span>AVTIL MAI 2016</span></div>

  <!-- Extensif -->
  <div class="label" style="left:20px;top:528px"><span class="tag">Extensif</span> Lundi/Mercredi/Vendredi</div>
  <section class="schedule" style="left:24px;top:570px;width:364px">
    <div class="schedule-date">25/04/2016 - 20/05/2016</div>
    <div class="schedule-times single">18H30-21H30</div>
    <div class="schedule-rows">
      <div><b>A1.1</b> DK2136</div><div><b>A2.2</b> DK2139</div>
      <div><b>A1.2</b> DK2137</div><div><b>B1.1</b> DK2140</div>
      <div><b>A2.1</b> DK2138</div><div><b>B1.2</b> DK2141</div>
    </div>
    <div class="schedule-foot"></div>
  </section>

  <!-- Intensif 1 -->
  <div class="label" style="left:467px;top:534px"><span class="tag">Intensif</span> Lundi - Vendredi</div>
  <section class="schedule" style="left:488px;top:576px;width:370px">
    <div class="schedule-date">18/04/2016 - 06/05/2016</div>
    <div class="schedule-times"><span>09H30 - 12H30</span><span>13H00 - 16H00</span></div>
    <div class="schedule-rows">
      <div><b>A1.1</b> DK2127</div><div><b>A2.2</b>DK2130</div>
      <div><b>A1.2</b> DK2128</div><div><b>B1.1</b> DK2131</div>
      <div><b>A2.1</b> DK2129</div><div><b>A1.1</b> DK2132</div>
      <div><b>B2.1</b> DK2134</div><div><b>B1.2</b> DK2133</div>
      <div><b>B2.2</b> DK2135</div><div></div>
    </div>
    <div class="schedule-foot thin"></div>
  </section>

  <!-- Intensif 2 -->
  <div class="label large" style="left:20px;top:815px"><span class="tag">Intensif</span> Intensif Lundi - Vendredi</div>
  <section class="schedule" style="left:24px;top:858px;width:364px">
    <div class="schedule-date">09/05/2016 - 27/05/2016</div>
    <div class="schedule-times"><span>09H30 - 12H30</span><span>13H00 - 16H00</span></div>
    <div class="schedule-rows">
      <div><b>A1.1</b> DK2142</div><div><b>B1.2</b> DK2147</div>
      <div><b>A1.2</b> DK2143</div><div><b>A1.1</b> DK2148</div>
      <div><b>A2.1</b> DK2144</div><div><b>A1.2</b> DK2149</div>
      <div><b>A2.2</b> DK2145</div><div><b>B2.1</b> DK2150</div>
      <div><b>B1.1</b> DK2146</div><div><b>B2.2</b> DK2151</div>
    </div>
    <div class="schedule-foot thin"></div>
  </section>

  <p class="notes">Toute inscription dolt im-perativement se faire au plus tard une semaine avant le debut des cours. Nombre mini-mum de 5 participants requis L'horaire des cours est sus-ceptible d'être modifie. Prix par module 340 TND.</p>

  <svg class="students" viewBox="0 0 380 282" role="img" aria-label="Photo: groupe de jeunes étudiants souriants levant le pouce">
    <defs>
      <linearGradient id="studentTone" x1="0" y1="0" x2="1" y2="0">
        <stop offset="0" stop-color="#e8d64a"/>
        <stop offset="0.4" stop-color="#8fb0c8"/>
        <stop offset="0.75" stop-color="#5f7c4a"/>
        <stop offset="1" stop-color="#d9534f"/>
      </linearGradient>
    </defs>
    <path d="M0,282 L0,120 Q60,20 130,30 Q200,-5 280,20 Q350,40 380,120 L380,282 Z" fill="url(#studentTone)" opacity="0.85"/>
  </svg>

  <footer class="footer">
    <div class="address">
      <svg class="icon" width="12" height="16" viewBox="0 0 12 16"><path d="M6 0a6 6 0 0 0-6 6c0 4.5 6 10 6 10s6-5.5 6-10a6 6 0 0 0-6-6zm0 8.5A2.5 2.5 0 1 1 6 3.5a2.5 2.5 0 0 1 0 5z" fill="var(--lime)"/></svg>
      <span>Imm. les Palmiers, 2eme étage 8 Rue du Lac Nakuru (en face de l'Hotel Lumière) 054 Les Rives du Lac 2</span>
    </div>
    <ul class="contacts">
      <li><svg class="icon" width="12" height="12" viewBox="0 0 12 12"><path d="M2.5 0.5l2 2.5-1.2 1.5a7 7 0 0 0 4.2 4.2L9 7.5l2.5 2-1 2C5.5 12 0 6.5 0.5 1.5z" fill="var(--lime)"/></svg>+216 71 000 482</li>
      <li><svg class="icon" width="12" height="10" viewBox="0 0 12 10"><rect x="0" y="0" width="12" height="10" rx="1" fill="var(--lime)"/><path d="M0.5 1l5.5 4.5L11.5 1" stroke="var(--ink)" fill="none"/></svg>tunis@linguora.org</li>
      <li><svg class="icon" width="12" height="12" viewBox="0 0 12 12"><circle cx="6" cy="6" r="5.5" fill="var(--lime)"/><path d="M0.5 6h11M6 0.5c-3 3-3 8 0 11M6 0.5c3 3 3 8 0 11" stroke="var(--ink)" stroke-width="0.8" fill="none"/></svg>www.linguora.org</li>
    </ul>
  </footer>

</main>
</body>
</html>
```